App Design

This is a 'video player' app - will be used to stream video files and watch them on a device. Need 3/4 skins for user customization.
Design will need to be versatile - used on: Kestrel4/4S/5 and vexTab2/3
Require an app design that shows the required functionality described by us, allows ease to navigate and visually creates a unique user experience.
App must have following pages: (refer to attached pages)
1. Search Page
2. Results Page
3. Video Page
4. End Page
3-4 skins for user preference
important: if you are interested please submit designs by tomorrow night - we will be picking from submitted designs - will make revisions and finalize the design within 4-5 days.
timing is crucial- please only submit if you can commit to timeline and design requirements. There will be refinements required.
Please see the attached update.
Additional reference files have been added to help in your efforts.
We have added a sample design that may help with your submissions. Please see brief
Target Market(s)
early adapters for technology / kestrel, tablet, zorbix users
Requirements
Should not have
- should not be generic design

```html
<!DOCTYPE html>
<html lang="en">
<head>
<meta charset="utf-8">
<title>Video Player App – Screens</title>
<link rel="stylesheet" href="https://fonts.googleapis.com/css2?family=Arimo:wght@400;700&display=swap">
<style>
  :root {
    --page-bg: #eef0f3;
    --blue-deep: #06127a;
    --blue-mid: #0b23b4;
    --blue-bright: #1540d8;
    --status-bg: #e9ebee;
    --status-text: #1b1b1b;
    --carrier-blue: #2a55d6;
    --tab-top: #555759;
    --tab-bottom: #1f2022;
    --tab-label: #d6d6d6;
    --tab-active: #6b6d70;
    --band-top: #c9d2e2;
    --band-bottom: #8c9ab5;
    --field-bg: #ffffff;
    --field-border: #7f8ba3;
    --placeholder: #9aa3b2;
    --button-top: #3a3a3a;
    --button-bottom: #050505;
    --strip-top: #e4e6ea;
    --strip-bottom: #b8bcc4;
    --row-bg: #ffffff;
    --row-line: #d5d7db;
    --row-text: #111111;
    --chevron: #2f6fe0;
    --white: #ffffff;
  }
  * { box-sizing: border-box; margin: 0; padding: 0; }
  html, body {
    width: 720px; height: 1200px; overflow: hidden;
    background: var(--page-bg);
    font-family: "Arimo", Arial, sans-serif;
  }
  .sprite { position: absolute; width: 0; height: 0; }

  .screen {
    position: absolute; width: 300px; height: 450px; overflow: hidden;
    background: linear-gradient(165deg, var(--blue-deep) 0%, var(--blue-mid) 55%, var(--blue-bright) 100%);
    box-shadow: 0 6px 18px rgba(0,0,0,.25);
  }
  .screen::before {
    content: ""; position: absolute; inset: 0; pointer-events: none;
    background: linear-gradient(118deg, transparent 55%, rgba(255,255,255,.08) 55%, rgba(255,255,255,.03) 80%, transparent 80%);
  }
  .screen--loading { left: 50px; top: 95px; }
  .screen--search  { left: 370px; top: 95px; }
  .screen--results { left: 50px; top: 655px; }
  .screen--video   { left: 370px; top: 655px; }

  .status-bar {
    position: absolute; left: 0; top: 0; width: 100%; height: 20px; z-index: 3;
    background: linear-gradient(var(--white), var(--status-bg));
    font-size: 10px; font-weight: 700; color: var(--status-text);
    display: flex; align-items: center; padding: 0 5px;
  }
  .status-bar__signal { display: flex; align-items: flex-end; gap: 1px; height: 9px; margin-right: 3px; }
  .status-bar__signal i { width: 2px; background: var(--carrier-blue); display: block; }
  .status-bar__carrier { color: #333; margin-right: 8px; }
  .status-bar__network { color: var(--carrier-blue); }
  .status-bar__time { position: absolute; left: 0; right: 0; text-align: center; pointer-events: none; }
  .status-bar__icons { margin-left: auto; display: flex; gap: 4px; align-items: center; }
  .battery { width: 20px; height: 9px; border: 1px solid #777; border-radius: 2px; padding: 1px; }
  .battery span { display: block; height: 100%; background: #39c43b; }

  .tab-bar {
    position: absolute; left: 0; bottom: 0; width: 100%; height: 48px; z-index: 3;
    background: linear-gradient(var(--tab-top), var(--tab-bottom));
    display: flex;
  }
  .tab {
    flex: 1; display: flex; flex-direction: column; align-items: center; justify-content: flex-end;
    padding-bottom: 5px; font-size: 8px; font-weight: 700; color: var(--tab-label);
    border-right: 1px solid rgba(0,0,0,.35);
  }
  .tab:last-child { border-right: 0; }
  .tab svg { width: 22px; height: 20px; margin-bottom: 4px; }
  .tab--active {
    background: linear-gradient(var(--tab-active), #3a3b3d);
    border-radius: 5px 5px 0 0; margin-top: -4px; color: var(--white);
  }

  .loader { position: absolute; left: 0; right: 0; top: 155px; text-align: center; }
  .loader__spinner { width: 44px; height: 44px; }
  .loader__text { margin-top: 14px; font-size: 15px; font-weight: 700; color: var(--white); }

  .search-band {
    position: absolute; left: 6px; right: 0; top: 150px; height: 54px;
    background: linear-gradient(var(--band-top), var(--band-bottom));
    border-radius: 3px 0 0 3px; padding: 15px 16px 0 12px;
  }
  .search-field {
    height: 24px; border-radius: 4px; background: var(--field-bg);
    border: 1px solid var(--field-border); box-shadow: inset 0 1px 3px rgba(0,0,0,.3);
    display: flex; align-items: center; justify-content: flex-end; padding: 0 6px;
    font-size: 11px; color: var(--placeholder);
  }
  .search-field span { margin-right: 18px; }
  .search-button {
    position: absolute; left: 91px; top: 225px; width: 100px; height: 36px;
    background: linear-gradient(var(--button-top), var(--button-bottom));
    border: 1px solid #888; border-radius: 4px; color: var(--white);
    font-size: 14px; font-weight: 700; display: flex; align-items: center; justify-content: center;
  }
  .thumb-strip {
    position: absolute; left: 0; bottom: 0; width: 100%; height: 74px;
    background: linear-gradient(var(--strip-top), var(--strip-bottom));
    display: flex; align-items: center; justify-content: space-between; padding: 0 4px;
  }
  .thumb-strip__arrow { width: 10px; height: 14px; fill: #9ea3ab; }
  .thumb-strip__items { display: flex; gap: 10px; }
  .thumb { width: 54px; height: 54px; border: 2px solid var(--white); box-shadow: 0 1px 3px rgba(0,0,0,.4); }

  .search-header {
    position: absolute; left: 0; top: 20px; width: 100%; height: 42px; z-index: 2;
    background: linear-gradient(#f4f5f7, #c4c8cf); border-bottom: 1px solid #9aa0aa;
    padding: 9px 20px 0 17px;
  }
  .search-pill {
    height: 24px; border-radius: 12px; background: var(--field-bg);
    border: 1px solid #8c93a0; box-shadow: inset 0 1px 3px rgba(0,0,0,.25);
    display: flex; align-items: center; padding-left: 7px; gap: 5px;
    font-size: 12px; color: var(--placeholder);
  }
  .search-pill svg { width: 12px; height: 12px; }

  .results-list { position: absolute; left: 0; top: 62px; width: 100%; bottom: 48px; background: var(--row-bg); overflow: hidden; }
  .result {
    height: 93px; display: flex; align-items: center; border-bottom: 1px solid var(--row-line);
    padding-left: 6px;
  }
  .result__thumb {
    width: 120px; height: 90px; background: #111; padding: 7px 6px;
    position: relative; flex-shrink: 0;
  }
  .result__thumb div { width: 100%; height: 100%; }
  .play-badge {
    position: absolute; left: 50%; top: 50%; width: 26px; height: 26px; margin: -13px 0 0 -13px;
  }
  .result__text {
    width: 130px; margin-left: 6px; font-size: 7.5px; line-height: 1.2; color: var(--row-text);
    text-align: justify;
  }
  .result__chevron { width: 16px; height: 16px; margin-left: 6px; flex-shrink: 0; }
  .scroll-indicator { position: absolute; right: 1px; top: 50px; width: 3px; height: 80px; border-radius: 2px; background: #b6b9be; }

  .video-frame {
    position: absolute; left: 19px; top: 98px; width: 262px; height: 172px;
    border: 4px solid var(--white); box-shadow: 0 2px 6px rgba(0,0,0,.4);
  }
  .video-frame div { width: 100%; height: 100%; background: radial-gradient(circle at 45% 45%, #b8c3b0, #6f8463 60%, #2f3b26); }
  .video-desc {
    position: absolute; left: 15px; right: 18px; top: 285px;
    font-size: 10px; line-height: 1.3; color: var(--white); text-align: justify;
  }
</style>
</head>
<body>

<svg class="sprite" aria-hidden="true">
  <symbol id="icon-heart" viewBox="0 0 24 22"><path d="M12 21 3 12a5 5 0 0 1 9-6 5 5 0 0 1 9 6z" fill="#c9cacc"/></symbol>
  <symbol id="icon-bulb" viewBox="0 0 24 22"><circle cx="12" cy="8" r="6.5" fill="#c9cacc"/><rect x="9" y="14" width="6" height="5" rx="1" fill="#9fa1a4"/></symbol>
  <symbol id="icon-cloud" viewBox="0 0 24 22"><path d="M6 18a4.5 4.5 0 0 1 0-9 6 6 0 0 1 11.5-1A5 5 0 0 1 18 18z" fill="#4fb6f0"/></symbol>
  <symbol id="icon-search" viewBox="0 0 24 22"><circle cx="14" cy="8" r="6" fill="none" stroke="#c9cacc" stroke-width="2.2"/><path d="M10 12 4 19" stroke="#c9cacc" stroke-width="2.6" stroke-linecap="round"/></symbol>
  <symbol id="icon-gear" viewBox="0 0 24 22"><circle cx="12" cy="11" r="6" fill="none" stroke="#c9cacc" stroke-width="4" stroke-dasharray="3 2.2"/><circle cx="12" cy="11" r="4.5" fill="none" stroke="#c9cacc" stroke-width="2"/></symbol>
  <symbol id="icon-play" viewBox="0 0 26 26"><circle cx="13" cy="13" r="12" fill="rgba(0,0,0,.75)" stroke="#fff" stroke-width="1"/><path d="M10 7.5 19 13l-9 5.5z" fill="#fff"/></symbol>
  <symbol id="icon-chevron" viewBox="0 0 16 16"><circle cx="8" cy="8" r="7.5" fill="var(--chevron)"/><path d="M6.5 4.5 10 8l-3.5 3.5" fill="none" stroke="#fff" stroke-width="2"/></symbol>
  <symbol id="icon-magnifier" viewBox="0 0 12 12"><circle cx="5" cy="5" r="3.6" fill="none" stroke="#7a808a" stroke-width="1.4"/><path d="M7.6 7.6 11 11" stroke="#7a808a" stroke-width="1.6"/></symbol>
</svg>

<section class="screen screen--loading">
  <header class="status-bar">
    <span class="status-bar__signal"><i style="height:3px"></i><i style="height:5px"></i><i style="height:7px"></i><i style="height:9px"></i></span>
    <span class="status-bar__carrier">NIMBUS</span><span class="status-bar__network">3G</span>
    <span class="status-bar__time">4:20 PM</span>
    <span class="status-bar__icons"><span class="battery"><span></span></span></span>
  </header>
  <div class="loader">
    <svg class="loader__spinner" viewBox="0 0 44 44" aria-hidden="true">
      <g stroke="#ffffff" stroke-width="4" stroke-linecap="round">
        <line x1="22" y1="4" x2="22" y2="12" opacity="1"/>
        <line x1="34.7" y1="9.3" x2="29.1" y2="14.9" opacity=".85"/>
        <line x1="40" y1="22" x2="32" y2="22" opacity=".7"/>
        <line x1="34.7" y1="34.7" x2="29.1" y2="29.1" opacity=".55"/>
        <line x1="22" y1="40" x2="22" y2="32" opacity=".45"/>
        <line x1="9.3" y1="34.7" x2="14.9" y2="29.1" opacity=".35"/>
        <line x1="4" y1="22" x2="12" y2="22" opacity=".25"/>
        <line x1="9.3" y1="9.3" x2="14.9" y2="14.9" opacity=".15"/>
      </g>
    </svg>
    <p class="loader__text">Loading.....</p>
  </div>
  <nav class="tab-bar">
    <div class="tab"><svg><use href="#icon-heart"/></svg>Favorites</div>
    <div class="tab"><svg><use href="#icon-bulb"/></svg>Idea</div>
    <div class="tab tab--active"><svg><use href="#icon-cloud"/></svg>Main label</div>
    <div class="tab"><svg><use href="#icon-search"/></svg>Search</div>
    <div class="tab"><svg><use href="#icon-gear"/></svg>More</div>
  </nav>
</section>

<section class="screen screen--search">
  <header class="status-bar">
    <span class="status-bar__signal"><i style="height:3px"></i><i style="height:5px"></i><i style="height:7px"></i><i style="height:9px"></i></span>
    <span class="status-bar__carrier">NIMBUS</span><span class="status-bar__network">3G</span>
    <span class="status-bar__time">4:20 PM</span>
    <span class="status-bar__icons"><span class="battery"><span></span></span></span>
  </header>
  <div class="search-band">
    <div class="search-field"><span>Enter your search here</span>
      <svg width="11" height="11" viewBox="0 0 12 12" aria-hidden="true"><path d="M10 6a4 4 0 1 1-1.2-2.8" fill="none" stroke="#7a808a" stroke-width="1.5"/><path d="M9.5 0.8v3h-3" fill="none" stroke="#7a808a" stroke-width="1.5"/></svg>
    </div>
  </div>
  <div class="search-button">Search</div>
  <div class="thumb-strip">
    <svg class="thumb-strip__arrow" viewBox="0 0 10 14"><path d="M9 1 1 7l8 6z"/></svg>
    <div class="thumb-strip__items">
      <div class="thumb" role="img" aria-label="Video thumbnail: animated character close-up" style="background:linear-gradient(135deg,#b5643a,#6a4630)"></div>
      <div class="thumb" role="img" aria-label="Video thumbnail: pink flower scene" style="background:linear-gradient(135deg,#8fb6dc,#c77fc6)"></div>
      <div class="thumb" role="img" aria-label="Video thumbnail: character in green forest" style="background:linear-gradient(135deg,#4e6a35,#9aa98c)"></div>
      <div class="thumb" role="img" aria-label="Video thumbnail: meadow under blue sky" style="background:linear-gradient(180deg,#7fb3e6,#8fb36a)"></div>
    </div>
    <svg class="thumb-strip__arrow" viewBox="0 0 10 14"><path d="M1 1l8 6-8 6z"/></svg>
  </div>
</section>

<section class="screen screen--results">
  <header class="status-bar">
    <span class="status-bar__signal"><i style="height:3px"></i><i style="height:5px"></i><i style="height:7px"></i><i style="height:9px"></i></span>
    <span class="status-bar__carrier">NIMBUS</span><span class="status-bar__network">3G</span>
    <span class="status-bar__time">4:20 PM</span>
    <span class="status-bar__icons"><span class="battery"><span></span></span></span>
  </header>
  <div class="search-header"><div class="search-pill"><svg><use href="#icon-magnifier"/></svg>Search</div></div>
  <div class="results-list">
    <article class="result">
      <div class="result__thumb"><div role="img" aria-label="Video still: animated character with a butterfly" style="background:linear-gradient(135deg,#8a6a4e,#c07fc8)"></div><svg class="play-badge"><use href="#icon-play"/></svg></div>
      <p class="result__text">Lorem ipsum dolor sit amet, consectetur adipiscing elit. Maecenas turpis nunc, blandit a mattis ut, sodales eu eros. Integer commodo interdum vulputate.</p>
      <svg class="result__chevron"><use href="#icon-chevron"/></svg>
    </article>
    <article class="result">
      <div class="result__thumb"><div role="img" aria-label="Video still: character in a sunny meadow" style="background:linear-gradient(180deg,#7eb4ea,#8db15c)"></div><svg class="play-badge"><use href="#icon-play"/></svg></div>
      <p class="result__text">Lorem ipsum dolor sit amet, consectetur adipiscing elit. Maecenas turpis nunc, blandit a mattis ut, sodales eu eros. Integer commodo interdum vulputate.</p>
      <svg class="result__chevron"><use href="#icon-chevron"/></svg>
    </article>
    <article class="result">
      <div class="result__thumb"><div role="img" aria-label="Video still: characters by a tree" style="background:linear-gradient(135deg,#6b5a3e,#9fbf5a)"></div><svg class="play-badge"><use href="#icon-play"/></svg></div>
      <p class="result__text">Lorem ipsum dolor sit amet, consectetur adipiscing elit. Maecenas turpis nunc, blandit a mattis ut, sodales eu eros. Integer commodo interdum vulputate.</p>
      <svg class="result__chevron"><use href="#icon-chevron"/></svg>
    </article>
    <article class="result">
      <div class="result__thumb"><div role="img" aria-label="Video still: characters by a tree" style="background:linear-gradient(135deg,#6b5a3e,#9fbf5a)"></div><svg class="play-badge"><use href="#icon-play"/></svg></div>
      <p class="result__text">Lorem ipsum dolor sit amet, consectetur adipiscing elit. Maecenas turpis nunc, blandit a mattis ut, sodales eu eros. Integer commodo interdum vulputate.</p>
      <svg class="result__chevron"><use href="#icon-chevron"/></svg>
    </article>
    <span class="scroll-indicator"></span>
  </div>
  <nav class="tab-bar">
    <div class="tab"><svg><use href="#icon-heart"/></svg>Favorites</div>
    <div class="tab"><svg><use href="#icon-bulb"/></svg>Idea</div>
    <div class="tab tab--active"><svg><use href="#icon-cloud"/></svg>Main label</div>
    <div class="tab"><svg><use href="#icon-search"/></svg>Search</div>
    <div class="tab"><svg><use href="#icon-gear"/></svg>More</div>
  </nav>
</section>

<section class="screen screen--video">
  <header class="status-bar">
    <span class="status-bar__signal"><i style="height:3px"></i><i style="height:5px"></i><i style="height:7px"></i><i style="height:9px"></i></span>
    <span class="status-bar__carrier">NIMBUS</span><span class="status-bar__network">3G</span>
    <span class="status-bar__time">4:20 PM</span>
    <span class="status-bar__icons"><span class="battery"><span></span></span></span>
  </header>
  <div class="search-header"><div class="search-pill"><svg><use href="#icon-magnifier"/></svg>Search</div></div>
  <div class="video-frame"><div role="img" aria-label="Video frame: animated character drawing a bow in a forest"></div></div>
  <p class="video-desc">Lorem ipsum dolor sit amet, consectetur adipiscing elit. Maecenas turpis nunc, blandit a mattis ut, sodales eu eros. Integer commodo interdum vulputate.</p>
  <nav class="tab-bar">
    <div class="tab"><svg><use href="#icon-heart"/></svg>Favorites</div>
    <div class="tab"><svg><use href="#icon-bulb"/></svg>Idea</div>
    <div class="tab tab--active"><svg><use href="#icon-cloud"/></svg>Main label</div>
    <div class="tab"><svg><use href="#icon-search"/></svg>Search</div>
    <div class="tab"><svg><use href="#icon-gear"/></svg>More</div>
  </nav>
</section>

</body>
</html>
```